velto renovation roof

We need a flyer for a new york based company called velto renovations. We are looking to promote our roofing/window/siding/concrete service.

We are a construction company with over 30 years in the business, but have set up a new company to specialize in roofing - windows - siding. We do offer general renovation service both interior (tiles, paint , Plakwall, etc) as well as concrete work (driveways, sidewalk) but we think it may be to much information for the flyer. We are fully insured and licensed

We are open to all ideas (I will include a picture of a design that caught our eye from your site).

Target Market(s)

home owners, building managers in the tri state area. We are a New York based company

Industry/Entity Type

Construction

```html
<!DOCTYPE html>
<html lang="en">
<head>
<meta charset="utf-8">
<title>Velto Renovations – Flyer</title>
<link rel="stylesheet" href="https://fonts.googleapis.com/css2?family=Archivo:ital,wght@0,800;1,800;1,900&family=Arimo:wght@400;700&family=Roboto+Condensed:wght@700&display=swap">
<style>
  :root {
    --brand-blue: #0a6edb;
    --photo-blue: #3a73c2;
    --photo-deep: #1f4f98;
    --navy: #0e1f3d;
    --ink-blue: #1c3a6e;
    --link-blue: #0a6edb;
    --white: #ffffff;
    --seal: #4a4a4f;
  }
  * { margin: 0; padding: 0; box-sizing: border-box; }
  html, body { width: 1200px; height: 1200px; overflow: hidden; background: var(--white); }
  .flyer { position: relative; width: 1200px; height: 1200px; font-family: "Arimo", Arial, sans-serif; }
  .panel { position: absolute; top: 0; width: 600px; height: 1200px; overflow: hidden; }
  .panel--front { left: 0; background: var(--white); }
  .panel--services { left: 600px; background: var(--white); }
  .shapes { position: absolute; inset: 0; width: 600px; height: 1200px; }

  .brand-title {
    position: absolute; left: 52px; top: 70px;
    font-family: "Archivo", Arial, sans-serif; font-weight: 900; font-style: italic;
    font-size: 45px; letter-spacing: 0.5px; color: var(--navy);
  }
  .rule { position: absolute; left: 52px; width: 500px; height: 3px; background: var(--white); }
  .rule--top { top: 367px; }
  .rule--bottom { top: 640px; }
  .service-list {
    position: absolute; left: 0; top: 392px; width: 600px; list-style: none; text-align: center;
    font-family: "Archivo", Arial, sans-serif; font-weight: 800; font-style: italic;
    font-size: 38px; line-height: 56px; color: var(--white);
    text-shadow: 0 2px 4px rgba(0,0,0,0.35); letter-spacing: 0.5px;
  }
  .seal { position: absolute; left: 185px; top: 685px; width: 210px; height: 210px; border-radius: 50%; background: var(--seal); }

  .contact { position: absolute; left: 0; width: 600px; text-align: center; }
  .contact__years { font-size: 36px; letter-spacing: 0.3px; }
  .contact__web, .contact__phone { font-size: 25px; margin-top: 8px; }
  .panel--front .contact { top: 1028px; }
  .panel--front .contact__years { color: var(--ink-blue); }
  .panel--front .contact__web { color: #222; }
  .panel--front .contact__phone { color: var(--link-blue); margin-top: 6px; }
  .panel--services .contact { top: 1038px; color: var(--white); }
  .panel--services .contact__web { margin-top: 12px; }

  .brand-small {
    position: absolute; left: 40px; top: 38px;
    font-family: "Archivo", Arial, sans-serif; font-weight: 900; font-style: italic;
    font-size: 16px; color: var(--white); letter-spacing: 0.3px;
  }
  .services-heading {
    position: absolute; left: 103px; top: 318px;
    font-family: "Roboto Condensed", Arial, sans-serif; font-weight: 700;
    font-size: 53px; color: var(--navy); letter-spacing: 1px;
  }
  .service { position: absolute; left: 100px; width: 460px; height: 100px; }
  .service__icon { position: absolute; left: 0; top: 0; width: 116px; height: 100px; }
  .service__text { position: absolute; left: 163px; font-size: 16.5px; line-height: 19px; }
  .service__name { font-family: "Roboto Condensed", Arial, sans-serif; font-weight: 700; color: var(--navy); font-size: 17px; letter-spacing: 0.3px; }
  .service__info { color: var(--link-blue); }
  .service--roofing { top: 408px; } .service--roofing .service__text { top: 30px; }
  .service--siding { top: 540px; } .service--siding .service__text { top: 4px; }
  .service--concrete { top: 628px; } .service--concrete .service__text { top: 4px; }
  .service--window { top: 730px; } .service--window .service__text { top: 22px; }
</style>
</head>
<body>
<main class="flyer">

  <section class="panel panel--front">
    <svg class="shapes" viewBox="0 0 600 1200" aria-hidden="false">
      <defs>
        <linearGradient id="house-photo" x1="0" y1="0" x2="0" y2="1">
          <stop offset="0" stop-color="#4d86d0"/>
          <stop offset="0.45" stop-color="var(--photo-blue)"/>
          <stop offset="1" stop-color="var(--photo-deep)"/>
        </linearGradient>
      </defs>
      <polygon role="img" aria-label="Photo of a brick house with a slate roof and white windows, tinted blue"
               points="0,180 200,285 600,155 600,880 240,1002 0,897" fill="url(#house-photo)"/>
    </svg>
    <h1 class="brand-title">VELTO RENOVATIONS</h1>
    <div class="rule rule--top"></div>
    <ul class="service-list">
      <li>ROOFING</li>
      <li>SIDING</li>
      <li>CONCRETE SERVICES</li>
      <li>WINDOW</li>
    </ul>
    <div class="rule rule--bottom"></div>
    <div class="seal" role="img" aria-label="Satisfaction guarantee seal"></div>
    <div class="contact">
      <p class="contact__years">30 YEARS IN BUSINESS</p>
      <p class="contact__web">www.VELTORENO.net</p>
      <p class="contact__phone">phone: 347-555-0184</p>
    </div>
  </section>

  <section class="panel panel--services">
    <svg class="shapes" viewBox="0 0 600 1200" aria-hidden="true">
      <polygon points="0,0 600,0 600,155 200,285 0,180" fill="var(--brand-blue)"/>
      <polygon points="0,897 200,1003 600,880 600,1200 0,1200" fill="var(--brand-blue)"/>
    </svg>
    <p class="brand-small">VELTO RENOVATIONS</p>
    <h2 class="services-heading">SERVICES</h2>

    <div class="service service--roofing">
      <svg class="service__icon" viewBox="0 0 116 100" aria-hidden="true">
        <path d="M2 58 L58 6 L114 58" fill="none" stroke="var(--navy)" stroke-width="12" stroke-linejoin="miter"/>
        <path d="M16 52 V100 H100 V52" fill="none" stroke="var(--navy)" stroke-width="10"/>
        <rect x="44" y="64" width="28" height="36" fill="var(--navy)"/>
      </svg>
      <div class="service__text"><p class="service__name">ROOFING</p><p class="service__info">Some information<br>regarding this</p></div>
    </div>

    <div class="service service--siding">
      <svg class="service__icon" viewBox="0 0 116 100" aria-hidden="true" fill="var(--navy)">
        <rect x="14" y="6" width="26" height="9"/><rect x="44" y="6" width="26" height="9"/><rect x="74" y="6" width="24" height="9"/>
        <rect x="14" y="19" width="11" height="9"/><rect x="29" y="19" width="26" height="9"/><rect x="59" y="19" width="26" height="9"/><rect x="89" y="19" width="9" height="9"/>
        <rect x="14" y="32" width="26" height="9"/><rect x="44" y="32" width="26" height="9"/><rect x="74" y="32" width="24" height="9"/>
        <rect x="14" y="45" width="11" height="9"/><rect x="29" y="45" width="26" height="9"/><rect x="59" y="45" width="26" height="9"/><rect x="89" y="45" width="9" height="9"/>
        <rect x="14" y="58" width="26" height="9"/><rect x="44" y="58" width="26" height="9"/><rect x="74" y="58" width="24" height="9"/>
      </svg>
      <div class="service__text"><p class="service__name">SIDING</p><p class="service__info">Some information<br>regarding this</p></div>
    </div>

    <div class="service service--concrete">
      <svg class="service__icon" viewBox="0 0 116 100" aria-hidden="true" fill="var(--navy)">
        <path d="M20 68 L42 50 L62 58 L50 70 Z"/>
        <path d="M48 56 L80 24" stroke="var(--navy)" stroke-width="3"/>
        <rect x="76" y="8" width="9" height="22" rx="4" transform="rotate(45 80 19)"/>
        <path d="M28 58 Q36 46 46 52 L40 60 Z"/>
      </svg>
      <div class="service__text"><p class="service__name">CONCRETE SERVICES</p><p class="service__info">Some information<br>regarding this</p></div>
    </div>

    <div class="service service--window">
      <svg class="service__icon" viewBox="0 0 116 100" aria-hidden="true">
        <rect x="2" y="6" width="112" height="6" fill="var(--navy)"/>
        <rect x="10" y="14" width="96" height="82" fill="none" stroke="var(--navy)" stroke-width="2"/>
        <line x1="58" y1="14" x2="58" y2="96" stroke="var(--navy)" stroke-width="2"/>
        <path d="M8 12 H44 Q36 40 22 52 Q26 76 22 96 H8 Z" fill="var(--navy)"/>
        <path d="M108 12 H72 Q80 40 94 52 Q90 76 94 96 H108 Z" fill="var(--navy)"/>
      </svg>
      <div class="service__text"><p class="service__name">WINDOW</p><p class="service__info">Some information<br>regarding this</p></div>
    </div>

    <div class="contact">
      <p class="contact__years">30 YEARS IN BUSINESS</p>
      <p class="contact__web">www.VELTORENO.net</p>
      <p class="contact__phone">phone: 347-555-0184</p>
    </div>
  </section>

</main>
</body>
</html>
```